Business cards for start-up accounting firm

I'm looking for a double sided business card ready for upload into Prontel ink or similar print providers with no modification required by me.
I'm looking for something simple as i think cards that are too 'busy' actually detract from the message. I have some thoughts but more than happy to see what comes up. The logo i have came out of left field and i love it the moment i saw it!

My thoughts:

Side 1: Just the logo, perhaps on a dark grey or charcoal background to make the logo colours stand out?

Side 2: The call to action from me website 'Looking for a more relaxed, friendly and interactive relationship with your accountant?' with my contact information
Name: Gavin Ormsby
Email: gavin@quellorix.com.au
Website: www.quellorix.com.au
Phone: 1300 742 916

The call to action needs to be the first thing they see when they look at side 2. If it helps to know what we do and how we do it there is a draft website at www.quellorix.com.au

Like i said, happy to consider anything that comes up :)

Target Market(s)

i'm targeting small business owners who experience a lot of stress around finacial reporting and have had bad experiences with accountants in the past.

Industry/Entity Type

Accounting

Contact Information for Business Card

Contained in the Description

Font styles to use
Serif
Sans Serif
Other font styles liked:
• See logo files attached

Colors
474747

Requirements
Must have
• My logo, slogan and contact information

```html
<!DOCTYPE html>
<html lang="en">
<head>
<meta charset="utf-8">
<title>Quellorix Business Cards</title>
<link href="https://fonts.googleapis.com/css2?family=Source+Sans+3:wght@400;600;700&display=swap" rel="stylesheet">
<style>
  :root {
    --stage: #000000;
    --card: #333538;
    --yellow: #f3d31a;
    --purple: #9c3a92;
    --rule: #7c7c82;
    --white: #f2f2f2;
  }
  * { margin: 0; padding: 0; box-sizing: border-box; }
  html, body { width: 1200px; height: 900px; overflow: hidden; background: var(--stage); }
  body { position: relative; font-family: "Source Sans 3", Arial, sans-serif; }

  .card {
    position: absolute; top: 271px; width: 457px; height: 281px;
    background: var(--card); border-radius: 14px; overflow: hidden;
  }
  .card--contact { left: 137px; }
  .card--brand { left: 626px; }

  .brand { position: absolute; left: 0; right: 0; text-align: center; }
  .brand__name {
    display: inline-flex; align-items: center; gap: 8px;
    color: var(--yellow); font-weight: 700; letter-spacing: 1px; line-height: 1;
  }
  .brand__dot { display: inline-block; border-radius: 50%; background: var(--purple); }

  .card--contact .brand { top: 50px; }
  .card--contact .brand__name { font-size: 38px; }
  .card--contact .brand__dot { width: 22px; height: 22px; }

  .card--brand .brand { top: 112px; }
  .card--brand .brand__name { font-size: 54px; }
  .card--brand .brand__dot { width: 30px; height: 30px; }

  .cta {
    position: absolute; top: 123px; left: 0; right: 0; text-align: center;
    color: var(--yellow); font-size: 16.5px; line-height: 20px;
  }
  .holder {
    position: absolute; top: 171px; left: 0; right: 0;
    display: flex; align-items: center; gap: 8px;
  }
  .holder::before, .holder::after { content: ""; flex: 1; height: 1px; background: var(--rule); }
  .holder__name { color: var(--purple); font-size: 17px; font-weight: 600; }

  .contacts { position: absolute; top: 200px; left: 0; right: 0; list-style: none; text-align: center; }
  .contacts__item {
    display: flex; align-items: center; justify-content: center; gap: 5px;
    color: var(--white); font-size: 13px; line-height: 19.5px;
  }
  .contacts__icon { width: 10px; height: 10px; fill: var(--yellow); }
</style>
</head>
<body>
  <section class="card card--contact">
    <div class="brand">
      <div class="brand__name">QUELLORIX<span class="brand__dot"></span></div>
    </div>
    <p class="cta">Looking for a more relaxed, helpful &amp; interactive<br>relationship with your Accountant?</p>
    <div class="holder"><span class="holder__name">Gavin Ormsby</span></div>
    <ul class="contacts">
      <li class="contacts__item">
        <svg class="contacts__icon" viewBox="0 0 10 10"><path d="M2 0.5 L3.6 2.6 L2.7 3.7 C3.3 5 4.8 6.6 6.3 7.3 L7.4 6.4 L9.5 8 L8.3 9.5 C4.5 9 1 5.5 0.5 1.7 Z"/></svg>
        1300 742 916
      </li>
      <li class="contacts__item">
        <svg class="contacts__icon" viewBox="0 0 10 10"><path d="M0.5 2 H9.5 V8.5 H0.5 Z M1 2.5 L5 5.6 L9 2.5" stroke="#333538" stroke-width="0.8"/></svg>
        gavin@quellorix.com.au
      </li>
      <li class="contacts__item">
        <svg class="contacts__icon" viewBox="0 0 10 10"><circle cx="5" cy="5" r="4.6"/><path d="M3 2.5 L5 3.5 L4.5 5.5 L2.5 5 Z M6 6 L7.8 6.5 L6.5 8.3 Z" fill="#333538"/></svg>
        www.quellorix.com.au
      </li>
    </ul>
  </section>

  <section class="card card--brand">
    <div class="brand">
      <div class="brand__name">QUELLORIX<span class="brand__dot"></span></div>
    </div>
  </section>
</body>
</html>
```